Business card design needed

We need a business card design for a new micro business based in Melbourne (Australia). Our main service is cleaning and fixing Vertical Blinds as a cheaper alternative than buying new blinds. A smaller part of the business is fitting affordable & temporary alternatives to double glazed windows both for noise abatement and climate control and reduction in energy costs.
We could be dealing with commercial as well as residential customers so we need a quality look. The design needs to reflect our core business of vertical blinds cleaning & maintenance.

Target Market(s)

Not sure yet. These Business Cards are going to be used to test the market

Industry/Entity Type

Residential

Contact Information for Business Card

Morlena Tazwick. Vertical Blinds Cleaning, Maintenance & Temporary Window Insulation Solutions. Ph: 03 7142 5063. Mob: 0471 356 249.

```html
<!DOCTYPE html>
<html lang="en">
<head>
<meta charset="utf-8">
<title>Morlena Tazwick – Business Card</title>
<link rel="stylesheet" href="https://fonts.googleapis.com/css2?family=Arvo:wght@400;700&display=swap">
<style>
  :root {
    --backdrop: #eceeee;
    --card-white: #ffffff;
    --charcoal: #2d2b2a;
    --orange: #f0801e;
    --orange-deep: #e06f12;
    --ink: #2a2828;
  }
  html, body {
    margin: 0;
    width: 1200px;
    height: 772px;
    overflow: hidden;
    background: var(--backdrop);
  }
  .card {
    position: absolute;
    left: 73px;
    top: 81px;
    width: 1025px;
    height: 591px;
    border-radius: 54px;
    overflow: hidden;
    background: var(--card-white);
    box-shadow: 0 4px 14px rgba(0,0,0,0.22);
    font-family: "Arvo", serif;
  }
  .hero-figure {
    position: absolute;
    left: 27px;
    top: 25px;
    width: 415px;
    height: 292px;
    background: linear-gradient(180deg, var(--orange) 0%, var(--orange-deep) 100%);
  }
  .accent-band {
    position: absolute;
    left: 0;
    top: 317px;
    width: 100%;
    height: 17px;
    background: var(--orange);
  }
  .base-panel {
    position: absolute;
    left: 0;
    top: 334px;
    width: 100%;
    bottom: 0;
    background: var(--charcoal);
  }
  .contact {
    position: absolute;
    left: 553px;
    top: 96px;
    color: var(--ink);
  }
  .contact-name {
    margin: 0 0 22px;
    font-size: 34px;
    font-weight: 400;
    line-height: 1;
  }
  .contact-line {
    display: flex;
    align-items: center;
    height: 60px;
    margin-left: 18px;
    font-size: 34px;
    font-weight: 700;
    letter-spacing: 1px;
  }
  .contact-line svg {
    width: 30px;
    height: 34px;
    margin-right: 20px;
    flex: none;
  }
  .tagline {
    position: absolute;
    left: 65px;
    top: 396px;
    width: 885px;
    margin: 0;
    color: #ffffff;
    font-size: 37px;
    font-weight: 700;
    line-height: 62px;
  }
  .tagline span {
    display: flex;
    justify-content: space-between;
  }
</style>
</head>
<body>
  <div class="card">
    <div class="hero-figure" role="img" aria-label="Orange silhouette of a worker adjusting vertical blinds"></div>
    <div class="accent-band"></div>
    <div class="base-panel"></div>

    <div class="contact">
      <p class="contact-name">Morlena Tazwick</p>
      <div class="contact-line">
        <svg viewBox="0 0 24 24" aria-hidden="true">
          <path fill="var(--orange)" d="M6.6 10.8c1.4 2.8 3.8 5.1 6.6 6.6l2.2-2.2c.3-.3.7-.4 1-.2 1.1.4 2.3.6 3.6.6.6 0 1 .4 1 1V20c0 .6-.4 1-1 1C10.6 21 3 13.4 3 4c0-.6.4-1 1-1h3.5c.6 0 1 .4 1 1 0 1.3.2 2.5.6 3.6.1.3 0 .7-.2 1L6.6 10.8z"/>
        </svg>
        03 7142 5063
      </div>
      <div class="contact-line">
        <svg viewBox="0 0 24 28" aria-hidden="true">
          <rect x="3" y="2" width="18" height="24" rx="3" fill="none" stroke="var(--orange)" stroke-width="2.4"/>
          <rect x="6" y="5.5" width="12" height="15" fill="var(--orange)"/>
          <circle cx="12" cy="23" r="1.3" fill="var(--orange)"/>
        </svg>
        0471 356 249
      </div>
    </div>

    <p class="tagline">
      <span><b>Vertical</b><b>Blinds</b><b>Cleaning,</b><b>Maintenance</b></span>
      <span><b>&amp;</b><b>Temporary</b><b>Window</b><b>Insulation</b><b>Solutions</b></span>
    </p>
  </div>
</body>
</html>
```